Create a Graphic About YOURSELF and PixelHarbor

PixelHarbor would like you (designers) to create an awesome graphic to promote YOURSELF and your profile on PixelHarbor!

Your graphic should communicate your name, your services and should mention PixelHarbor.

The design should be perfect for sharing on Chatterly. Here's an example of what we'd like http://blog.pixelharbor-example.ca/article/333/pixelharbor-launches-3000-hire-me-social-design-contest

Once you submitted your design, we'd love you to share the design ('advertisement') and promote yourself and PixelHarbor to your friends and potential customers. So make your submissions great and get your friends to vote for your design by 'Liking' it on Chatterly!

Prizes:
$1500 - "PixelHarbor Community" prize awarded to the designer with the most Chatterly 'Likes'
5 x $50 for the next 5 'most liked' designs on Chatterly

$1000 - "Hire Me" prize awarded to the designer who receives the most client invites
5 x $50 for the next 5 'most invited' designers

In summary, this is a great opportunity for you to increase your exposure to PixelHarbor customers and win cash prizes. Show off your design skills and get hired by PixelHarbor customers from around the world!

Target Market(s)

Fans, friends and customers of YOU

Industry/Entity Type

Cash

Requirements
Must have
• 1) Include your PixelHarbor user name on the graphic so customers can find you in the PixelHarbor Designer Directory
2) Include the tagline "Hire Me on PixelHarbor.com!" in your graphic design.
3) Share your design's URL on our Chatterly wall at http://chatterly-example.com/pixelharbor and get your friends to 'like' your design.
Nice to have
• 1) Include a tagline that expresses your design approach/philosophy
2) Artwork dimensions: 403 x 403 px
3) You can submit more than 1 design!
Should not have
• You must own the copyright of any images you use including stock imagery.

```html
<!DOCTYPE html>
<html lang="en">
<head>
<meta charset="utf-8">
<title>Want to change the scale? – Hire me on PixelHarbor</title>
<link rel="stylesheet" href="https://fonts.googleapis.com/css2?family=Fredoka:wght@500;600;700&family=Roboto+Condensed:wght@400;700&display=swap">
<style>
  :root {
    --paper: #ffffff;
    --backdrop-tint: #eef1f4;
    --ink-dark: #1c2430;
    --accent-blue: #1f8fd6;
    --sphere-light: #3fb3ea;
    --sphere-deep: #1272b8;
    --brand-red: #d7161f;
    --navy: #16375e;
  }
  html, body {
    margin: 0;
    padding: 0;
    width: 1200px;
    height: 1200px;
    overflow: hidden;
    background: var(--paper);
  }
  .promo-canvas {
    display: block;
    width: 1200px;
    height: 1200px;
  }
  .headline {
    font-family: "Fredoka", sans-serif;
    font-weight: 700;
    font-size: 25px;
    fill: var(--ink-dark);
  }
  .headline .highlight { fill: var(--accent-blue); }
  .you-label {
    font-family: "Fredoka", sans-serif;
    font-weight: 600;
    fill: var(--accent-blue);
  }
  .designer-name {
    font-family: "Fredoka", sans-serif;
    font-weight: 700;
    font-size: 27px;
    fill: var(--brand-red);
  }
  .services-line {
    font-family: "Roboto Condensed", sans-serif;
    font-weight: 400;
    font-size: 12px;
    fill: var(--ink-dark);
  }
  .hire-small {
    font-family: "Fredoka", sans-serif;
    font-weight: 600;
    font-size: 10px;
    fill: var(--navy);
  }
  .hire-brand {
    font-family: "Fredoka", sans-serif;
    font-weight: 600;
    font-size: 20px;
    fill: var(--navy);
  }
  .pointer-line { stroke: var(--accent-blue); stroke-width: 0.8; fill: none; }
</style>
</head>
<body>
<svg class="promo-canvas" viewBox="0 0 403 403" xmlns="http://www.w3.org/2000/svg">
  <defs>
    <radialGradient id="backdrop-fill" cx="0.5" cy="0.5" r="0.7">
      <stop offset="0" stop-color="var(--paper)"/>
      <stop offset="1" stop-color="var(--backdrop-tint)"/>
    </radialGradient>
    <radialGradient id="sphere-fill" cx="0.45" cy="0.42" r="0.65">
      <stop offset="0" stop-color="var(--sphere-light)"/>
      <stop offset="1" stop-color="var(--sphere-deep)"/>
    </radialGradient>
  </defs>

  <rect class="backdrop-area" width="403" height="403" fill="url(#backdrop-fill)"
        role="img" aria-label="Pale grey abstract backdrop shapes"/>

  <!-- headline -->
  <text class="headline" x="26" y="42">want to <tspan class="highlight">CHANGE</tspan></text>
  <text class="headline" x="78" y="69">the <tspan class="highlight">SCALE</tspan>?</text>

  <!-- sphere illustration area -->
  <g class="sphere-illustration" role="img" aria-label="Illustration of a large blue glossy sphere with white bubbles and a soft shadow">
    <circle cx="201" cy="198" r="118" fill="url(#sphere-fill)"/>
  </g>

  <!-- you label -->
  <text class="you-label" x="47" y="141" font-size="8">THIS IS</text>
  <text class="you-label" x="47" y="154" font-size="11">You</text>
  <path class="pointer-line" d="M62 156 Q 78 158 90 164"/>

  <!-- designer identity -->
  <text class="designer-name" x="14" y="371">KORVEL</text>
  <text class="services-line" x="14" y="388">Logo/web/packaging/stationary...</text>

  <!-- hire me -->
  <text class="hire-small" x="264" y="369">Hire me on</text>
  <circle class="brand-dot" cx="249" cy="381" r="6" fill="var(--navy)"/>
  <text class="hire-brand" x="260" y="388">PixelHarbor</text>
</svg>
</body>
</html>
```